Health care startup that needs to WOW bone marrow doctors with presentation brochure

We need a brochure to compliment our in person presentation to Transplant Hospital Directors. The design needs to feel contemporary and clean. We need to convey a very professional operation that embraces technology. We want to break in as a modern company in an industry that has historically been non-profit and a little dull.

Our website is corvantix.com

I've included an early brochure we had from our site. We like our logo. The "Corvantix blue" in the logo is #7CD9DA in Microsoft Office products

I envision the brochure having two folds to reveal three pages. Ive added some of the text and images we will use.

The charts and graphs included in the attached ppt. can be modified by the designer but we want to capture the information in the final design.

Target Market(s)

Transplant Center Physicians

Industry/Entity Type

Healthcare

Colors
85cae6

Requirements
Must have
• a foldout brochure with at least three pages.
• Emphasis on our key competitive advantages, minority donors (80%), predominantly male (70%) and average age 21. This needs to be emphasized.
• I want to show that we will be a cost leader in the industry as well.
Nice to have
• I like the idea of a pocket or some means to attach a personal letter to clients on the inside. Not sure if that would work with the flow of the document.
• Websites whose design we LOVE:
• http://www.drelvonsuite.com/solutions/overview/
• http://quorelbay.com/
Should not have
• I dont want plain stock photos of people looking straight at a camera smiling. This feels like a non-profit trying to elict sympathy. Compassion for patients in a core value of the company, but it should still feel like something that is modern and new and a change to the current industry

```html
<!DOCTYPE html>
<html lang="en">
<head>
<meta charset="utf-8">
<title>Corvantix Brochure</title>
<link href="https://fonts.googleapis.com/css2?family=Open+Sans:wght@300;400;600;700&display=swap" rel="stylesheet">
<style>
:root{
  --sky:#85cae6;
  --sky-text:#7cc3e3;
  --ink:#3a3a3a;
  --ink-soft:#555;
  --stage:#d2d3d5;
  --paper:#ffffff;
  --photo-gray:#8e9094;
}
*{margin:0;padding:0;box-sizing:border-box}
html,body{width:1200px;height:1052px;overflow:hidden;background:var(--stage)}
body{font-family:'Open Sans',sans-serif;color:var(--ink)}
.canvas{position:relative;width:1200px;height:1052px}
.panel{position:absolute;width:367px;height:475px;overflow:hidden}
.panel--white{background:var(--paper)}
.panel--sky{background:var(--sky)}
.abs{position:absolute}
.section-title{font-weight:300;font-size:15px;color:var(--sky-text)}
.body-copy{font-size:7.1px;line-height:10px;color:var(--ink)}
.brand{display:flex;align-items:center;gap:6px;font-weight:400;letter-spacing:2px;color:var(--ink)}
.brand__dot{width:14px;height:14px;border:1.3px solid var(--sky-text);border-radius:50%}
.stat__num{font-weight:700;font-size:16px;color:var(--sky-text);text-align:center}
.stat__label{font-size:8px;color:var(--ink);text-align:center;margin-top:3px}
.photo{position:absolute;left:0;width:367px}
.photo-title{position:absolute;color:#fff;font-weight:400;font-size:20px}
.highlight{position:absolute;left:107px;display:flex;gap:7px;font-size:7.5px;line-height:10.2px;color:var(--ink);width:240px}
.highlight__dot{flex:none;width:9px;height:9px;border:1px solid var(--sky-text);border-radius:50%;margin-top:0}
.url{position:absolute;font-size:11px;color:var(--sky-text)}
.side-heading{position:absolute;left:44px;color:#fff;font-weight:300;font-size:14px;line-height:17.5px}
.ethnic{position:absolute;text-align:center;color:#fff;width:70px}
.ethnic__num{font-weight:700;font-size:17px;line-height:20px}
.ethnic__label{font-size:6.5px}
.feature{position:absolute;width:86px;text-align:center}
.feature__icon{display:block;margin:0 auto 6px}
.feature__title{font-weight:700;font-size:9.5px;color:var(--sky-text);line-height:10px}
.feature__text{font-size:6.6px;line-height:8.6px;color:var(--ink)}
</style>
</head>
<body>
<div class="canvas">

  <!-- Top left: mission -->
  <section class="panel panel--white" style="left:47px;top:43px">
    <svg class="abs" style="left:43px;top:47px" width="16" height="14" viewBox="0 0 16 14"><path d="M0 0 L16 7 L6 8 L4 14 Z" fill="#3a4a5a"/></svg>
    <h2 class="abs section-title" style="left:75px;top:43px">Our Mission</h2>
    <p class="abs body-copy" style="left:75px;top:71px;width:258px">Corvantix believes that all bone marrow transplant patients should have a donor match delivered on time at an affordable price. To that end we are building a world class registry to aid Transplant Centers in treating their ethnic minority patients. We are committed to proving customer service excellence second to none.</p>
    <div class="abs brand" style="left:74px;top:168px;font-size:14px"><span class="brand__dot"></span>CORVANTIX</div>
    <svg class="abs" style="left:56px;top:241px" width="14" height="16" viewBox="0 0 14 16"><circle cx="7" cy="5" r="4" fill="#3a4a5a"/><path d="M0 16 Q0 9 7 9 Q14 9 14 16 Z" fill="#3a4a5a"/></svg>
    <h2 class="abs section-title" style="left:75px;top:237px">What we Do</h2>
    <p class="abs body-copy" style="left:75px;top:266px;width:258px">As a total transplant procurement solution, Corvantix vertically integrates as a registry and donation center to maximize efficiency and provide operational excellence to deliver marrow/PBSCs on time - at industry leading prices. Corvantix harnesses industry leading best practices to target, recruit, and maintain active donors with unprecedented donor follow through rates. Transplant Center clients access these donors through our web based software, Lumaris. Once identified as a potential match, Corvantix guides donors through CT, workup, and collection. We then personally deliver the product to our transplant center clients.</p>
    <div class="abs" style="left:75px;top:388px;width:80px"><div class="stat__num">80%</div><div class="stat__label">minority donors</div></div>
    <div class="abs" style="left:160px;top:388px;width:90px"><div class="stat__num">70%</div><div class="stat__label">predominantly male</div></div>
    <div class="abs" style="left:275px;top:388px;width:60px"><div class="stat__num">21</div><div class="stat__label">average age</div></div>
  </section>

  <!-- Top middle: back cover -->
  <section class="panel panel--sky" style="left:415px;top:43px;color:#fff;text-align:center">
    <div class="abs brand" style="left:135px;top:294px;font-size:16px;color:#fff"><span class="brand__dot" style="border-color:#fff"></span>CORVANTIX</div>
    <p class="abs" style="left:0;width:367px;top:359px;font-size:10px">Get Started Today</p>
    <p class="abs" style="left:0;width:367px;top:385px;font-size:10px;line-height:13px">Please contact us to learn more:<br>4820 Alder Row, NW | Harwick | DC | 20041<br>P 555.014.2290<br>www.corvantix.com</p>
  </section>

  <!-- Top right: front cover -->
  <section class="panel panel--white" style="left:782px;top:43px">
    <div class="abs brand" style="left:60px;top:84px;font-size:19px"><span class="brand__dot" style="width:17px;height:17px"></span>CORVANTIX</div>
    <div class="photo" role="img" aria-label="Photo of a donor resting with headphones during donation" style="top:133px;height:271px;background:linear-gradient(120deg,#7d7f83,#a2a4a7 55%,#8b8d90)"></div>
    <p class="abs" style="right:34px;top:330px;text-align:right;color:#fff;font-size:19px;line-height:23px">The solution to bone<br><strong style="font-weight:700">marrow donor shortages.</strong></p>
    <p class="url" style="right:34px;top:438px">www.corvantix.com</p>
  </section>

  <!-- Bottom left: highlights -->
  <section class="panel panel--white" style="left:47px;top:536px">
    <div class="photo" role="img" aria-label="Photo of clinicians reviewing notes together, tinted blue" style="top:15px;height:164px;background:linear-gradient(100deg,#9ed3ea,#bfe2f1 50%,#a8d8ec)"></div>
    <h2 class="photo-title" style="left:46px;top:142px">Highlights</h2>
    <div class="highlight" style="top:207px"><span class="highlight__dot"></span>100% domestically sourced donor base</div>
    <div class="highlight" style="top:227px"><span class="highlight__dot"></span>Emphasis on African Americans and Hispanic males in the 18-25 year old demographic</div>
    <div class="highlight" style="top:258px"><span class="highlight__dot"></span>Reduced cycle time resulting from our co-location strategy</div>
    <div class="highlight" style="top:288px"><span class="highlight__dot"></span>24/7 access to a designated Corvantix donation coordinator from confirmatory typing through delivery to Transplant Center</div>
    <div class="highlight" style="top:329px"><span class="highlight__dot"></span>Industry cost leader</div>
    <div class="highlight" style="top:349px"><span class="highlight__dot"></span>Secure, user friendly web site to easily access and search the Corvantix donor database and track the progress of current donations</div>
    <div class="highlight" style="top:389px"><span class="highlight__dot"></span>Courier service by Corvantix employees</div>
    <p class="url" style="left:60px;top:443px">www.corvantix.com</p>
  </section>

  <!-- Bottom middle: cost leader -->
  <section class="panel panel--sky" style="left:415px;top:536px">
    <div class="photo" role="img" aria-label="Photo of a medical team reviewing a document" style="top:15px;height:164px;background:linear-gradient(100deg,#85878b,#a4a6a9 55%,#909296)"></div>
    <h2 class="photo-title" style="left:44px;top:142px">Cost leader in the industry</h2>
    <p class="side-heading" style="top:210px">Donor<br>Recruitment<br>Results</p>
    <p class="abs" style="left:191px;top:203px;font-size:8.5px;color:#fff">Number of Recruited Donors</p>
    <svg class="abs" style="left:185px;top:219px" width="150" height="120" viewBox="0 0 150 120" font-family="Open Sans, sans-serif" font-size="6" fill="#fff">
      <g stroke="#d8eef8" stroke-width="0.8">
        <line x1="25" y1="10" x2="138" y2="10"/><line x1="25" y1="29" x2="138" y2="29"/><line x1="25" y1="49" x2="138" y2="49"/><line x1="25" y1="68" x2="138" y2="68"/><line x1="25" y1="87" x2="138" y2="87"/>
      </g>
      <g text-anchor="end"><text x="19" y="12">2,000</text><text x="19" y="31">1,500</text><text x="19" y="51">1,000</text><text x="19" y="70">500</text><text x="19" y="89">0</text></g>
      <polyline points="31,87 43,87 63,83 79,75 95,61 111,45 131,27" fill="none" stroke="#fff" stroke-width="2.2" stroke-linejoin="round"/>
      <g text-anchor="end">
        <text transform="translate(33,95) rotate(-50)">Oct</text><text transform="translate(47,95) rotate(-50)">Nov</text><text transform="translate(63,95) rotate(-50)">Dec</text><text transform="translate(81,95) rotate(-50)">Jan</text><text transform="translate(97,95) rotate(-50)">Feb</text><text transform="translate(112,95) rotate(-50)">March</text><text transform="translate(128,95) rotate(-50)">April</text>
      </g>
    </svg>
    <p class="side-heading" style="top:377px">Donor<br>Ethnicity<br>Composition</p>
    <div class="ethnic" style="left:183px;top:355px"><div class="ethnic__num">18%</div><div class="ethnic__label">White/Caucasian</div></div>
    <div class="ethnic" style="left:250px;top:355px"><div class="ethnic__num">4%</div><div class="ethnic__label">Asian</div></div>
    <div class="ethnic" style="left:183px;top:394px"><div class="ethnic__num">6%</div><div class="ethnic__label">Hispanic/Latino</div></div>
    <div class="ethnic" style="left:250px;top:394px"><div class="ethnic__num">72%</div><div class="ethnic__label">Black/African</div></div>
  </section>

  <!-- Bottom right: why choose -->
  <section class="panel panel--white" style="left:782px;top:536px">
    <h2 class="abs" style="left:0;width:390px;text-align:center;top:23px;font-size:15px;font-weight:400;color:var(--ink)">Why Choose Corvantix</h2>
    <div class="feature" style="left:37px;top:55px">
      <svg class="feature__icon" width="18" height="18" viewBox="0 0 18 18"><circle cx="9" cy="9" r="7.5" fill="none" stroke="#4a4a4a" stroke-width="2"/><path d="M5 9 L8 12 L15 4" fill="none" stroke="#4a4a4a" stroke-width="2.2"/></svg>
      <div class="feature__title">Efficient</div>
      <div class="feature__text">Increase donor availability from our domestically sourced registry; Reducing cycle time from donor contact to HCT/P delivery.</div>
    </div>
    <div class="feature" style="left:144px;top:55px">
      <svg class="feature__icon" width="18" height="18" viewBox="0 0 18 18"><circle cx="9" cy="9" r="7.5" fill="none" stroke="#4a4a4a" stroke-width="1.8"/><circle cx="9" cy="9" r="4" fill="none" stroke="#4a4a4a" stroke-width="1.8"/><circle cx="9" cy="9" r="1.3" fill="#4a4a4a"/><path d="M9 9 L17 1" stroke="#4a4a4a" stroke-width="1.6"/></svg>
      <div class="feature__title">Targeted</div>
      <div class="feature__text">Donor base recruitment focusing on minority males (18-25 year old).</div>
    </div>
    <div class="feature" style="left:246px;top:55px">
      <svg class="feature__icon" width="18" height="18" viewBox="0 0 18 18"><circle cx="9" cy="9" r="7.5" fill="none" stroke="#4a4a4a" stroke-width="1.8"/><text x="9" y="11" font-size="5" font-weight="700" text-anchor="middle" fill="#4a4a4a" font-family="Open Sans, sans-serif">24/7</text></svg>
      <div class="feature__title">Responsive</div>
      <div class="feature__text">24/7 access to a personal Corvantix donation coordinator from initial match to HCT/P delivery.</div>
    </div>
    <div class="feature" style="left:92px;top:163px">
      <svg class="feature__icon" width="16" height="18" viewBox="0 0 16 18"><circle cx="8" cy="7" r="6" fill="none" stroke="#4a4a4a" stroke-width="1.6"/><path d="M6 13 V17 H10 V13" fill="none" stroke="#4a4a4a" stroke-width="1.6"/></svg>
      <div class="feature__title">Intelligent</div>
      <div class="feature__text">Secure, intuitive website to easily search the Corvantix database and monitor donations in progress.</div>
    </div>
    <div class="feature" style="left:188px;top:163px">
      <svg class="feature__icon" width="16" height="18" viewBox="0 0 16 18"><circle cx="8" cy="5" r="4" fill="#4a4a4a"/><path d="M0 18 Q0 10 8 10 Q16 10 16 18 Z" fill="#4a4a4a"/></svg>
      <div class="feature__title">Professional</div>
      <div class="feature__text">HCT/P transport provided by a dedicated Corvantix team member.</div>
    </div>
    <svg class="abs" style="left:0;top:0" width="367" height="475" viewBox="0 0 367 475"><polygon points="58,333 368,333 368,475 7,475" fill="var(--sky)"/></svg>
  </section>

</div>
</body>
</html>
```